Redesign of Business Card to look more professional and stand out

Business card design. You can lean more about our company by going to dkrfabworks.example. Raised letters would be nice. Company name & Address
DK&R
418 Wendlow Ridge Drive, Suite 340
Kelterbrook, GA 30899

You can use my name and title: Glenn Harwick
Business Development Manager

Target Market(s)

Heavy Industrial market, i.e. utilities, chemical plants, paper mills, construction companies

Industry/Entity Type

Construction

Contact Information for Business Card

We provide Project Management & Project Support Services

Font styles to use
Serif

Requirements
Must have
• Company name & Address
• DK&R
• 418 Wendlow Ridge Drive, Suite 340
• Kelterbrook, GA 30899
Nice to have
• ideas for the back of the card
Should not have
• no crazy colors. needs to look professional and standout.

```html
<!DOCTYPE html>
<html lang="en">
<head>
<meta charset="utf-8">
<title>DK&amp;R Business Card</title>
<link rel="stylesheet" href="https://fonts.googleapis.com/css2?family=Open+Sans:wght@400;700;800&display=swap">
<style>
  :root {
    --navy: #1c3a6d;
    --navy-back: #213f78;
    --navy-raised: #1a3566;
    --ink: #2b2b2b;
    --paper: #ffffff;
    --stage: #e9e7e3;
  }
  * { margin: 0; padding: 0; box-sizing: border-box; }
  html, body {
    width: 1200px;
    height: 900px;
    overflow: hidden;
    background: var(--stage);
    font-family: "Open Sans", Arial, sans-serif;
  }
  .canvas {
    width: 1200px;
    height: 900px;
    display: flex;
    flex-direction: column;
    align-items: center;
    justify-content: center;
    gap: 36px;
  }
  .card {
    width: 700px;
    height: 400px;
    position: relative;
    box-shadow: 0 2px 10px rgba(0,0,0,0.18);
  }
  /* Back side */
  .card-back {
    background: var(--navy-back);
    display: flex;
    align-items: center;
    justify-content: center;
  }
  .back-wordmark {
    font-weight: 800;
    font-size: 118px;
    letter-spacing: 2px;
    color: var(--navy-raised);
    line-height: 1;
  }
  /* Front side */
  .card-front {
    background: var(--paper);
    color: var(--ink);
  }
  .contact {
    position: absolute;
    left: 330px;
    top: 42px;
    text-transform: uppercase;
    font-size: 15px;
    line-height: 1.3;
  }
  .contact-name {
    color: var(--navy);
    font-weight: 700;
    font-size: 19px;
    letter-spacing: 0.3px;
  }
  .contact-title { margin-left: 10px; }
  .contact-company {
    color: var(--navy);
    font-weight: 700;
    font-size: 19px;
    margin-top: 16px;
    margin-left: 36px;
  }
  .contact-address { margin-left: 36px; }
  .contact-web {
    display: flex;
    align-items: center;
    gap: 12px;
    margin-top: 38px;
    margin-left: 72px;
  }
  .contact-web svg { width: 18px; height: 18px; flex: none; }
  .front-wordmark {
    position: absolute;
    left: 40px;
    bottom: 34px;
    font-weight: 800;
    font-size: 104px;
    letter-spacing: 1px;
    color: var(--navy);
    line-height: 1;
  }
</style>
</head>
<body>
<main class="canvas">
  <section class="card card-back" aria-label="Card back">
    <span class="back-wordmark">DK&amp;R</span>
  </section>

  <section class="card card-front" aria-label="Card front">
    <div class="contact">
      <p class="contact-name">Glenn Harwick</p>
      <p class="contact-title">Business Development Manager</p>
      <p class="contact-company">DK&amp;R</p>
      <p class="contact-address">418 Wendlow Ridge Drive, Suite 340</p>
      <p class="contact-address">Kelterbrook, GA 30899</p>
      <p class="contact-web">
        <svg viewBox="0 0 20 20" aria-hidden="true">
          <circle cx="10" cy="10" r="9" fill="var(--navy)"/>
          <ellipse cx="10" cy="10" rx="4" ry="8" fill="none" stroke="#fff" stroke-width="1.3"/>
          <line x1="2" y1="10" x2="18" y2="10" stroke="#fff" stroke-width="1.3"/>
        </svg>
        <span>www.dkrfabworks.example</span>
      </p>
    </div>
    <span class="front-wordmark">DK&amp;R</span>
  </section>
</main>
</body>
</html>
```